chocolate bar wrapper

Need a design for a new line of chocolate bars being sold at new retail candy store concept called PLINKTREATS. There will be many flavors including Dark Chocolate, Milk Chocolate, Dark Chocolate Espresso, Milk Chocolate Smores, Dark Chocolate Strawberry Champagne, Dark Chocolate Sea Salt, Dark Chocolate Chipotle, etc. Size of bar is 3 inches x 6 5/8 inches.

Please visit PLINKTREATS.EXAMPLE

Industry/Entity Type

Retail

```html
<!DOCTYPE html>
<html lang="en">
<head>
<meta charset="utf-8">
<title>PlinkTreats — Dark Chocolate Espresso Wrapper</title>
<link rel="stylesheet" href="https://fonts.googleapis.com/css2?family=Alfa+Slab+One&family=Anton&display=swap">
<style>
  :root {
    --cocoa: #4a2a0c;
    --white: #ffffff;
    --pink: #e77fb8;
    --yellow: #f3e936;
    --lime: #c2dc72;
    --sky: #5cc8f2;
    --coral: #ef5a55;
    --rose: #ee5a92;
    --orange: #f7941e;
    --violet: #9a6bb5;
    --brand-red: #e8303a;
  }
  html, body {
    margin: 0;
    padding: 0;
    overflow: hidden;
    background: var(--white);
  }
  .wrapper {
    position: relative;
    width: 1200px;
    height: 543px;
    overflow: hidden;
    font-family: "Alfa Slab One", Georgia, serif;
  }
  .burst-backdrop {
    position: absolute;
    inset: 0;
    background:
      radial-gradient(ellipse at 78% 92%, rgba(74, 42, 12, 0.25), transparent 45%),
      linear-gradient(160deg, var(--sky) 0%, var(--yellow) 28%, var(--lime) 62%, var(--lime) 100%),
      var(--yellow);
  }
  .burst-backdrop::after {
    content: "";
    position: absolute;
    inset: 0;
    background: linear-gradient(100deg, transparent 45%, rgba(238, 90, 146, 0.75) 62%, rgba(92, 200, 242, 0.7) 80%, rgba(154, 107, 181, 0.75) 100%);
  }
  .flavor-title {
    position: absolute;
    left: 0;
    top: 0;
    width: 1200px;
    height: 320px;
  }
  .flavor-title text {
    font-family: "Alfa Slab One", Georgia, serif;
    font-size: 92px;
    stroke-linejoin: round;
  }
  .flavor-title .outer { fill: var(--pink); stroke: var(--pink); stroke-width: 22px; }
  .flavor-title .inner { fill: var(--cocoa); stroke: var(--cocoa); stroke-width: 12px; }
  .flavor-title .face  { fill: var(--white); }
  .brand-name {
    position: absolute;
    left: 540px;
    top: 358px;
    width: 560px;
    margin: 0;
    text-align: center;
    font-size: 72px;
    line-height: 1;
    color: var(--brand-red);
    letter-spacing: 1px;
  }
  .brand-tagline {
    position: absolute;
    left: 540px;
    top: 466px;
    width: 560px;
    margin: 0;
    text-align: center;
    font-family: "Anton", Impact, sans-serif;
    font-size: 34px;
    line-height: 1;
    color: var(--cocoa);
    letter-spacing: 1px;
  }
</style>
</head>
<body>
  <main class="wrapper">
    <div class="burst-backdrop" role="img" aria-label="Colourful sunburst rays in yellow, green, pink, blue and orange separated by chocolate-brown stripes"></div>

    <svg class="flavor-title" viewBox="0 0 1200 320" aria-label="Dark Chocolate Espresso">
      <g class="outer">
        <text x="48" y="168">Dark Chocolate</text>
        <text x="1112" y="282" text-anchor="end">Espresso</text>
      </g>
      <g class="inner">
        <text x="48" y="168">Dark Chocolate</text>
        <text x="1112" y="282" text-anchor="end">Espresso</text>
      </g>
      <g class="face">
        <text x="48" y="168">Dark Chocolate</text>
        <text x="1112" y="282" text-anchor="end">Espresso</text>
      </g>
    </svg>

    <p class="brand-name">PLINKTREATS</p>
    <p class="brand-tagline">ICE CREAM, CHOCOLATES &amp; CANDY!</p>
  </main>
</body>
</html>
```